Looking for awesome business card design with attached existing logo

We are a water, mold, and fire damage restoration company called "Torvane Seco" Looking for an awesome business card that is edgy yet professional and unique. Show me what you got!

```html
<!DOCTYPE html>
<html lang="en">
<head>
<meta charset="utf-8">
<title>Torvane Seco – Business Card</title>
<link href="https://fonts.googleapis.com/css2?family=Montserrat:wght@500;600;700;800&display=swap" rel="stylesheet">
<style>
  :root {
    --stage: #2b2c2e;
    --teal: #2b4a5a;
    --teal-raised: #33566a;
    --navy: #24465a;
    --gold: #e09a1c;
    --paper: #ffffff;
  }
  * { margin: 0; padding: 0; box-sizing: border-box; }
  html, body { width: 1200px; height: 939px; overflow: hidden; }
  body {
    background: var(--stage);
    font-family: 'Montserrat', sans-serif;
    position: relative;
  }
  .card {
    position: absolute;
    width: 600px;
    height: 343px;
    border-bottom: 3px solid var(--gold);
    border-right: 2px solid var(--gold);
    box-shadow: 0 14px 30px rgba(0,0,0,.45);
  }
  .card-back {
    left: 110px; top: 80px;
    background: var(--teal);
    display: flex; align-items: center; justify-content: center;
  }
  .back-mark {
    display: flex; align-items: center; gap: 14px;
    color: var(--teal-raised);
    font-weight: 800; font-size: 46px; letter-spacing: 1px;
    text-transform: uppercase;
  }
  .back-mark .dot {
    width: 18px; height: 18px; border-radius: 50%;
    background: var(--teal-raised);
  }
  .card-front {
    left: 490px; top: 520px;
    background: var(--paper);
  }
  .brand {
    position: absolute; left: 30px; top: 150px;
    width: 270px;
    display: flex; align-items: center; justify-content: center; gap: 10px;
    color: var(--navy);
    font-weight: 800; font-size: 24px; letter-spacing: .3px;
    text-transform: uppercase;
    white-space: nowrap;
  }
  .brand .dot {
    width: 13px; height: 13px; border-radius: 50%;
    background: var(--gold); flex: none;
  }
  .divider {
    position: absolute; left: 318px; top: 62px;
    width: 2px; height: 200px;
    background: linear-gradient(var(--navy) 0 18%, transparent 18% 24%, var(--gold) 24% 76%, transparent 76% 82%, var(--navy) 82% 100%);
  }
  .details {
    position: absolute; left: 340px; top: 60px;
    color: var(--navy);
    font-size: 11.5px; font-weight: 600; line-height: 1.45;
  }
  .person-name {
    color: var(--gold); font-weight: 800; font-size: 20px;
    text-transform: uppercase; letter-spacing: .3px;
  }
  .person-role { font-size: 12px; margin-bottom: 10px; }
  .address { margin-bottom: 10px; }
  .contact { list-style: none; }
  .contact li { display: flex; align-items: center; gap: 7px; }
  .contact svg { width: 11px; height: 11px; flex: none; }
  .contact .accent { color: var(--gold); }
  .services {
    position: absolute; left: 340px; top: 282px;
    color: var(--navy); font-weight: 600; font-size: 14px;
    letter-spacing: .5px;
  }
  .services .sep { color: var(--gold); font-weight: 800; padding: 0 5px; }
</style>
</head>
<body>
  <section class="card card-back" aria-label="Card back">
    <div class="back-mark"><span class="dot"></span>Torvane Seco</div>
  </section>

  <section class="card card-front" aria-label="Card front">
    <div class="brand"><span class="dot"></span>Torvane Seco</div>
    <div class="divider"></div>
    <div class="details">
      <div class="person-name">Daniel Varko</div>
      <div class="person-role">Founder and President</div>
      <div class="address">48 Harlow Lane, Ground Floor<br>Brookfield, NY 10217</div>
      <ul class="contact">
        <li>
          <svg viewBox="0 0 12 12"><path d="M2.5 1l2 2.2-1 1.3a7 7 0 0 0 4 4l1.3-1 2.2 2-1.2 1.5C5 10.5 1.5 7 1 2.2z" fill="var(--gold)"/></svg>
          <span>+1 (555) 284-1907</span>
        </li>
        <li>
          <svg viewBox="0 0 12 12"><rect x="1" y="2.5" width="10" height="7" fill="var(--gold)"/><path d="M1 2.5l5 4 5-4" stroke="#fff" stroke-width="1" fill="none"/></svg>
          <span>info@<span class="accent">torvaneseco</span>.com</span>
        </li>
        <li>
          <svg viewBox="0 0 12 12"><circle cx="6" cy="6" r="4.7" fill="none" stroke="var(--gold)" stroke-width="1.2"/><path d="M1.3 6h9.4M6 1.3c-2.4 2.6-2.4 6.8 0 9.4M6 1.3c2.4 2.6 2.4 6.8 0 9.4" stroke="var(--gold)" stroke-width=".8" fill="none"/></svg>
          <span>www.<span class="accent">torvaneseco</span>.com</span>
        </li>
      </ul>
    </div>
    <div class="services">WATER<span class="sep">|</span>MOLD<span class="sep">|</span>FIRE</div>
  </section>
</body>
</html>
```